Real Estate Design Website

I would like to have a design for "real estate agent" website. It needs to be in a "Responsive" framework.

The design need to be suitable for different viewer from all around the world. It needs to be modern. It'd be great if there is a design for mobile and vexo/tablet (it's all under responsive framework). It needs to be easy to navigate and look modern

Target Market(s)

End user/Real estate buyers from different part of the world

Industry/Entity Type

Real Estate

Requirements
Must have
• It's for real estate agent website which is used to represent their brand/image but at the same time it also for their client which is real estate buyers
Should not have
• Should not be boring design/out of date

```html
<!DOCTYPE html>
<html lang="en">
<head>
<meta charset="utf-8">
<title>Hearthline Realty</title>
<link href="https://fonts.googleapis.com/css2?family=Oswald:wght@300;400;500&family=Roboto:wght@400;500&family=Roboto+Condensed:wght@400&display=swap" rel="stylesheet">
<style>
:root{
  --orange:#f7941d;
  --orange-deep:#e8650c;
  --gold:#f6b21a;
  --charcoal:#2f2f2f;
  --panel:#1c1c1c;
  --ink:#333;
  --muted:#888;
  --light:#f2f2f2;
  --rule:#dcdcdc;
  --link:#3c8ed4;
  --fb:#3b5fa3;
  --tw:#1ec4f2;
  --li:#2b9bd3;
}
*{margin:0;padding:0;box-sizing:border-box}
html,body{width:1155px;height:1200px;overflow:hidden;background:#e6e6e6;font-family:Roboto,Arial,sans-serif}
.page{position:relative;width:1155px;height:1200px}
.abs{position:absolute}

/* header */
.header{left:0;top:0;width:1155px;height:125px;background:linear-gradient(#3a3a3a,#2c2c2c)}
.navbar{left:0;top:86px;width:1155px;height:39px;background:#2a2a2a;border-top:1px solid #444;border-bottom:1px solid #1a1a1a}
.brand{left:198px;top:28px;font-family:Oswald,sans-serif;font-weight:400;font-size:34px;color:#fff;letter-spacing:1px;display:flex;align-items:center;gap:10px}
.brand-mark{width:16px;height:16px;background:var(--orange)}
.lang-label{left:751px;top:31px;font-family:Oswald,sans-serif;font-size:13px;color:var(--gold)}
.lang-select{left:881px;top:30px;width:71px;height:20px;border-radius:4px;background:var(--orange);color:#fff;font-size:10px;padding:4px 0 0 11px}
.lang-select::after{content:"";position:absolute;right:8px;top:8px;border:5px solid transparent;border-top-color:#fff;border-bottom:0}
.social-dot{top:66px;width:38px;height:38px;border-radius:50%;background:#333;border:3px solid #222;box-shadow:0 0 0 1px #555}
.nav{left:380px;top:86px;height:39px;display:flex;font-family:Oswald,sans-serif;font-size:16px;color:#fff}
.nav a{color:#fff;text-decoration:none;padding:9px 12px 0;height:39px}
.nav a.current{background:#222;color:var(--orange);padding:9px 16px 0;margin-right:12px}

/* hero */
.hero-bg{left:0;top:125px;width:1155px;height:312px;background:linear-gradient(135deg,#4a4a4a,#333 50%,#444)}
.band{left:0;top:437px;width:1155px;height:183px;background:linear-gradient(var(--orange),var(--orange-deep))}
.band-edge{left:0;top:620px;width:1155px;height:7px;background:#2e2e2e}
.hero-frame{left:177px;top:135px;width:541px;height:346px;background:#111;padding:5px}
.hero-photo{width:100%;height:100%;background:linear-gradient(100deg,#3a5a8a 0%,#2b3a55 18%,#6e6a62 40%,#a9a398 65%,#d8d6d0 85%,#8a8780)}
.search{left:727px;top:135px;width:259px;height:346px;background:var(--panel)}
.search h2{position:absolute;left:19px;top:13px;font-family:Oswald,sans-serif;font-weight:400;font-size:17px;line-height:22px;color:var(--gold)}
.field{position:absolute;left:19px;font-family:Oswald,sans-serif;font-size:11px;line-height:14px;color:#aaa;letter-spacing:.5px}
.select{position:absolute;height:22px;background:#2b2b2b;border:1px solid #3a3a3a;color:#777;font-size:10px;line-height:12px;font-style:italic;padding:4px 8px}
.select::after{content:"";position:absolute;right:0;top:0;width:15px;height:20px;background:#555}
.toggle-rent{left:112px;top:108px;height:24px;font-family:Oswald,sans-serif;font-size:16px;line-height:24px;color:var(--gold)}
.toggle-sale{left:152px;top:108px;width:66px;height:24px;background:var(--orange);color:#fff;font-family:Oswald,sans-serif;font-size:16px;text-align:center;line-height:24px}
.slider{left:21px;top:230px;width:210px;height:26px;border-radius:13px;background:#333;border:2px solid #2a2a2a}
.slider-line{position:absolute;left:10px;right:10px;top:10px;height:2px;background:#8ab8e8}
.knob{position:absolute;top:5px;width:11px;height:11px;border-radius:50%;background:#eee}
.ticks{left:21px;top:267px;width:210px;display:flex;justify-content:space-between;font-size:7px;line-height:8px;color:#8ab8e8;padding:0 4px}
.find{left:39px;top:302px;width:168px;height:29px;background:linear-gradient(#3c3c3c,#2a2a2a);border:1px solid #555;border-radius:3px;color:#2ab7f0;font-family:Georgia,serif;font-size:10px;text-align:center;line-height:28px}

/* categories */
.cat{top:497px;display:flex;align-items:center;gap:10px}
.cat-circle{width:112px;height:112px;border-radius:50%;background:radial-gradient(#fff,#e6e6e6);border:4px solid #f7c590}
.cat-art{width:60px;height:60px;margin:22px;border-radius:8px}
.cat-label{font-family:Oswald,sans-serif;color:#fff;line-height:1}
.cat-label small{display:block;font-size:15px;font-weight:400;margin-bottom:2px}
.cat-label big{display:block;font-size:50px;font-weight:400}

/* featured */
.featured{left:0;top:627px;width:1155px;height:116px;background:linear-gradient(#fff,#f0f0f0);border-bottom:1px solid #ddd}
.featured h2{position:absolute;left:0;width:1155px;top:8px;text-align:center;font-family:Oswald,sans-serif;font-weight:400;font-size:22px;color:#333}
.arrow{position:absolute;top:52px}
.thumb{position:absolute;top:44px;width:102px;height:58px;border:2px solid #ccc}

/* blog */
.blog-bg{left:0;top:744px;width:1155px;height:271px;background:#fff}
.blog-head{left:192px;top:770px;font-family:Oswald,sans-serif;font-size:23px;color:#333;font-weight:400}
.blog-head em{font-style:italic;color:#888;font-weight:300;margin-right:10px}
.blog-img{left:190px;top:827px;width:192px;height:121px;padding:4px;background:#ddd}
.blog-img div{width:100%;height:100%;background:linear-gradient(#c8ccd2,#5a5e66 60%,#7a3a3e)}
.post-meta{left:394px;top:834px;width:298px;font-size:11px;font-style:italic;color:#999;display:flex;justify-content:space-between}
.post-meta span b{color:var(--gold);font-weight:500}
.post-meta span:first-child{color:var(--gold)}
.post-body{left:394px;top:857px;width:306px;font-size:10px;line-height:15px;color:#444}
.post-body p+p{margin-top:15px}
.read-more{left:394px;top:987px;font-size:11px;font-weight:500;color:var(--gold)}

.discuss{left:722px;top:760px;width:264px;height:255px;background:#e5e5e5;padding:5px 8px 0}
.discuss h3{height:62px;background:#f2f2f2;font-family:Oswald,sans-serif;font-weight:400;font-size:22px;color:#333;padding:12px 16px}
.topic{background:#fff;border-top:1px solid #ddd;height:60px;padding:14px 0 0 34px;position:relative;font-size:11px;color:#333}
.topic:nth-of-type(even){background:#f6f6f6}
.topic::before{content:"";position:absolute;left:14px;top:17px;width:12px;height:9px;border-radius:50%;background:#555}
.topic small{display:flex;gap:22px;margin-top:5px;font-size:9px;color:#999;font-style:italic}
.topic small a{color:var(--link);text-decoration:none;font-style:normal}

/* follow */
.follow{left:0;top:1015px;width:1155px;height:105px;background:#e9e9e9}
.follow h2{position:absolute;top:14px;width:1155px;text-align:center;font-family:Oswald,sans-serif;font-weight:400;font-size:22px;color:#333}
.btn{position:absolute;top:51px;width:123px;height:37px;color:#fff;font-size:13px;font-weight:500;display:flex;align-items:center;border:1px solid rgba(0,0,0,.2)}
.btn i{width:12px;height:12px;background:#fff;margin:0 18px 0 14px;border-radius:2px}
.btn.fb{left:382px;background:var(--fb)}
.btn.tw{left:520px;background:var(--tw)}
.btn.li{left:658px;background:var(--li)}

.footer{left:0;top:1120px;width:1155px;height:48px;background:linear-gradient(#111,#000);border-top:3px solid #c9a36a}
.footer-links{left:179px;top:1141px;font-size:10px;color:#ccc}
.copyright{left:764px;top:1139px;font-size:10px;color:#ccc}
</style>
</head>
<body>
<div class="page">
  <header class="abs header"></header>
  <div class="abs navbar"></div>
  <div class="abs brand"><span class="brand-mark"></span>Hearthline Realty</div>
  <div class="abs lang-label">SELECT YOUR LANGUAGE:</div>
  <div class="abs lang-select">English</div>
  <div class="abs social-dot" style="left:827px"></div>
  <div class="abs social-dot" style="left:869px"></div>
  <div class="abs social-dot" style="left:910px"></div>
  <nav class="abs nav">
    <a class="current" href="#">HOME</a><a href="#">PROPERTIES</a><a href="#">NEWS</a><a href="#">BLOG</a><a href="#">PAGES</a><a href="#">CONTACT</a>
  </nav>

  <div class="abs hero-bg"></div>
  <div class="abs band"></div>
  <div class="abs band-edge"></div>
  <div class="abs hero-frame"><div class="hero-photo" role="img" aria-label="Modern hotel-style bedroom with balcony view over the city at dusk"></div></div>

  <form class="abs search">
    <h2>SEARCH FOR HOMES</h2>
    <div class="field" style="top:76px">LOCATION</div>
    <div class="select" style="left:92px;top:62px;width:148px">All locations</div>
    <div class="field" style="top:113px">TRANSACTION</div>
    <div class="abs toggle-rent">RENT</div>
    <div class="abs toggle-sale">SALE</div>
    <div class="field" style="top:180px">NO. OF ROOMS</div>
    <div class="select" style="left:92px;top:168px;width:67px">Beds</div>
    <div class="select" style="left:166px;top:168px;width:66px">Baths</div>
    <div class="field" style="top:210px">SEARCH RADIUS</div>
    <div class="abs slider"><div class="slider-line"></div><span class="knob" style="left:16px"></span><span class="knob" style="left:183px"></span></div>
    <div class="abs ticks"><span>0</span><span>2Mil</span><span>4Mil</span><span>6Mil</span><span>8Mil</span></div>
    <div class="abs find">
      <svg width="10" height="10" viewBox="0 0 10 10" style="vertical-align:-1px;margin-right:4px"><circle cx="4" cy="4" r="3" fill="none" stroke="#2ab7f0" stroke-width="1.6"/><line x1="6.2" y1="6.2" x2="9.3" y2="9.3" stroke="#2ab7f0" stroke-width="1.8"/></svg>FIND PROPERTIES</div>
  </form>

  <div class="abs cat" style="left:195px">
    <div class="cat-circle"><div class="cat-art" role="img" aria-label="House icon" style="background:linear-gradient(#333,#ddd)"></div></div>
    <div class="cat-label"><small>PROPERTIES FOR</small><big>SALE</big></div>
  </div>
  <div class="abs cat" style="left:442px">
    <div class="cat-circle"><div class="cat-art" role="img" aria-label="Glass office building icon" style="background:linear-gradient(#bfe6ee,#3a9bb0)"></div></div>
    <div class="cat-label"><small>PROPERTIES FOR</small><big>RENT</big></div>
  </div>
  <div class="abs cat" style="left:686px">
    <div class="cat-circle"><div class="cat-art" role="img" aria-label="Townhouse icon" style="background:linear-gradient(#d9b58a,#8a5a32)"></div></div>
    <div class="cat-label"><small>PROPERTIES FOR</small><big>LEASE</big></div>
  </div>

  <section class="abs featured">
    <h2>FEATURED PROPERTIES ON SALE</h2>
    <svg class="arrow" style="left:186px" width="18" height="16" viewBox="0 0 18 16"><path d="M8 1 1 8l7 7M1 8h16" fill="none" stroke="#111" stroke-width="3"/></svg>
    <svg class="arrow" style="left:932px" width="18" height="16" viewBox="0 0 18 16"><path d="M10 1l7 7-7 7M17 8H1" fill="none" stroke="#111" stroke-width="3"/></svg>
    <div class="thumb" style="left:218px;background:linear-gradient(#ddd6c8,#8a6a4a)" role="img" aria-label="Furnished bedroom"></div>
    <div class="thumb" style="left:337px;background:linear-gradient(#eef0f4,#9a4a3a)" role="img" aria-label="Red brick apartment block"></div>
    <div class="thumb" style="left:456px;background:linear-gradient(#e8eaee,#a04a36)" role="img" aria-label="Brick townhouse facade"></div>
    <div class="thumb" style="left:573px;background:linear-gradient(#9cc0e6,#8a7a66 55%,#5f8a3a)" role="img" aria-label="Houses beside a lawn"></div>
    <div class="thumb" style="left:692px;background:linear-gradient(#d8d2c4,#5a5048)" role="img" aria-label="Study room with desk"></div>
    <div class="thumb" style="left:812px;background:linear-gradient(#dfe8f0,#8a6a56 55%,#7a9a4a)" role="img" aria-label="Apartment building with garden"></div>
  </section>

  <div class="abs blog-bg"></div>
  <h2 class="abs blog-head"><em>From the Blog:</em>BEST PROPERTIES OF SUMMER 2013</h2>
  <div class="abs blog-img"><div role="img" aria-label="Bright living room with red sofa and wide windows"></div></div>
  <div class="abs post-meta"><span>Posted by: <b>kestrelhomes</b></span><span>Tue, Aug 14,12</span></div>
  <div class="abs post-body">
    <p>Lorem ipsum dolor sit amet, consectetuer adipiscing elit, sed diam nonummy nibh euismod tincidunt ut laoreet dolore magna aliquam erat volutpat. Ut wisi enim ad minim veniam, quis nostrud exerci tation ullamcorper suscipit lobortis nisl ut aliquip ex</p>
    <p>ea commodo consequat.im ad minim veniam, quis nostrud exerci tation ullamcorper suscipit lobortis nisl ut aliquip ex ea commodo consequat.im ad minim veniam, quis nos</p>
  </div>
  <a class="abs read-more">Continue Reading »</a>

  <aside class="abs discuss">
    <h3>LATEST DISCUSSIONS:</h3>
    <div class="topic">Praesent id metus massa, utblandit.<small><span>by <a>Lena Ortiz</a></span><span>2012-08-14 14:30:16</span></small></div>
    <div class="topic">Praesent id metus massa, utblandit.<small><span>by <a>Lena Ortiz</a></span><span>2012-08-14 14:30:16</span></small></div>
    <div class="topic">Praesent id metus massa, utblandit.<small><span>by <a>Lena Ortiz</a></span><span>2012-08-14 14:30:16</span></small></div>
  </aside>

  <section class="abs follow">
    <h2>FOLLOW US</h2>
    <a class="btn fb"><i></i>like us!</a>
    <a class="btn tw"><i></i>follow us</a>
    <a class="btn li"><i></i>follow us</a>
  </section>

  <footer class="abs footer"></footer>
  <div class="abs footer-links">Villas for Sale • Apartments for Rent • Office Space • Search for one • Latest offers</div>
  <div class="abs copyright">Copyright © Hearthline Realty. All Rights Reserved.</div>
</div>
</body>
</html>
```